Lumora Wellness - Professional Sales Presentation

Lumora Wellness needs to take it's professional sales presentation to the next level. The finished product must be engaging, elegant and trustworthy. In 20 slides or less, our value proposition needs to be crisply communicated. We will be using this presentation for Webinars and in print form, so this project requires a designer with deep powerpoint presentation experience. Both are very important ... 1) How the presentation is revealed live, and 2) How it appears in print form.

I've attached a draft presentation along with AI and JPG versions of our logo. Please visit LumoraWellness.example for insight on our services. Be certain to watch the video on our home page to learn what we do ... you'll be inspired! The winning presentation will be presented in boardrooms at Meridian 700 companies across America.

I'll interact frequently with those who take this project seriously and bring their very best work to the table ... you'll be working directly with Lumora's CEO.

You're invited to knock my socks off :)

Gregor

Target Market(s)

Meridian 700 Executives - the head of Benefits or Human Resources

Industry/Entity Type

Health Care

Font styles to use
Sans Serif
Script

Colors
ec1f27

Requirements
Must have
• Must be very professional, but creatively engaging, no more than 20 slides. Board rooms are inundated with BORING presentations ... that can't be this one. It needs to stand out, without going over the top.
Nice to have
• I need to be able to edit the text you'll find in my DRAFT presentation so please don't just create and use graphic files. Feel free to create cool graphic elements that are revealed at various points, but the next needs to be editable throughout.
Should not have
• Can't be cheesy, cheap or gimmicky. Must be completely credible.

```html
<!DOCTYPE html>
<html lang="en">
<head>
<meta charset="utf-8">
<title>Lumora Wellness – Some other important facts</title>
<link rel="stylesheet" href="https://fonts.googleapis.com/css2?family=Arimo:wght@400;700&display=swap">
<style>
  :root {
    --brand-red: #ec1f27;
    --deep-red: #b5121b;
    --band-red: #ee2b2e;
    --band-orange: #f39c17;
    --band-green: #95b851;
    --band-teal: #16a085;
    --band-blue: #2a80b9;
    --text-dark: #1e1e1e;
    --text-grey: #7a7a7a;
    --paper: #ffffff;
  }
  html, body {
    margin: 0;
    padding: 0;
    overflow: hidden;
    background: var(--paper);
  }
  .slide {
    position: relative;
    width: 1200px;
    height: 900px;
    overflow: hidden;
    background: var(--paper);
    font-family: "Arimo", Arial, sans-serif;
    color: var(--text-dark);
  }
  .swoosh {
    position: absolute;
    left: 0;
    top: 0;
    width: 1200px;
    height: 900px;
  }
  .slide-title {
    position: absolute;
    left: 222px;
    top: 40px;
    margin: 0;
    font-size: 43px;
    font-weight: 400;
    color: var(--brand-red);
    letter-spacing: 0.2px;
  }
  .profile-graphic {
    position: absolute;
    left: 175px;
    top: 237px;
    width: 395px;
    height: 432px;
    border-radius: 150px 120px 40px 20px;
    background: linear-gradient(to bottom,
      var(--band-red) 0%, var(--band-red) 17%,
      var(--band-orange) 23%, var(--band-orange) 36%,
      var(--band-green) 43%, var(--band-green) 57%,
      var(--band-teal) 63%, var(--band-teal) 77%,
      var(--band-blue) 83%, var(--band-blue) 100%);
  }
  .step-number {
    position: absolute;
    left: 325px;
    width: 60px;
    text-align: center;
    font-size: 25px;
    font-weight: 700;
    color: var(--paper);
  }
  .fact {
    position: absolute;
    left: 585px;
    display: flex;
    align-items: flex-start;
  }
  .fact-marker {
    flex: none;
    width: 56px;
    height: 56px;
    border-radius: 6px;
  }
  .fact-text {
    margin: -8px 0 0 22px;
    width: 495px;
    font-size: 15px;
    line-height: 20.5px;
    color: var(--text-dark);
  }
  .fact--1 { top: 206px; }
  .fact--2 { top: 319px; }
  .fact--3 { top: 425px; }
  .fact--4 { top: 550px; }
  .fact--5 { top: 669px; }
  .fact--1 .fact-marker { background: var(--band-red); }
  .fact--2 .fact-marker { background: var(--band-orange); }
  .fact--3 .fact-marker { background: var(--band-green); }
  .fact--4 .fact-marker { background: var(--band-teal); }
  .fact--5 .fact-marker { background: var(--band-blue); }
  .brand-name {
    position: absolute;
    left: 44px;
    top: 852px;
    font-size: 20px;
    font-weight: 700;
    color: var(--brand-red);
  }
  .footer-copyright {
    position: absolute;
    left: 720px;
    top: 864px;
    font-size: 13px;
    color: var(--text-grey);
  }
  .footer-url {
    position: absolute;
    left: 1036px;
    top: 862px;
    font-size: 14px;
    color: var(--brand-red);
  }
</style>
</head>
<body>
<div class="slide">
  <svg class="swoosh" viewBox="0 0 1200 900" aria-hidden="true">
    <path d="M165 0 L215 0 C90 230 60 520 420 900 L395 900 C20 560 40 250 165 0 Z" fill="var(--brand-red)"/>
    <path d="M120 480 C110 650 200 790 320 900 L245 900 C150 800 105 650 120 480 Z" fill="var(--deep-red)"/>
  </svg>

  <h1 class="slide-title">Some other important facts…</h1>

  <div class="profile-graphic" role="img" aria-label="Head profile silhouette divided into five coloured bands, one per fact"></div>
  <div class="step-number" style="top:262px">01</div>
  <div class="step-number" style="top:346px">02</div>
  <div class="step-number" style="top:430px">03</div>
  <div class="step-number" style="top:522px">04</div>
  <div class="step-number" style="top:610px">05</div>

  <div class="fact fact--1">
    <span class="fact-marker"></span>
    <p class="fact-text">Our diagnostic finger-stick testing technology meets all clinical standards for labs and is used by hospitals, urgent care centers and the Federal Defense Agency. Lumora has exclusive rights for use at worksites for employers and health plans.</p>
  </div>
  <div class="fact fact--2">
    <span class="fact-marker"></span>
    <p class="fact-text">You can choose who to target for these Virtual Preventive Checkups every year vs. every 1-5 years, thus avoiding over-testing and unnecessary PCP visits</p>
  </div>
  <div class="fact fact--3">
    <span class="fact-marker"></span>
    <p class="fact-text">Most employers choose to offer them annually for everyone because 80% of the population are either overweight, obese, smokers, nutritionally unsound, non-exercisers, or have chronic conditions (and for tracking changes/improvements year-over-year)</p>
  </div>
  <div class="fact fact--4">
    <span class="fact-marker"></span>
    <p class="fact-text">There are not enough PCPs in bricks-and-mortar settings to serve everyone who needs periodic Preventive Checkups</p>
  </div>
  <div class="fact fact--5">
    <span class="fact-marker"></span>
    <p class="fact-text">Individual testing results, including NP action plan, are securely sent to the patient’s smart phone (Pocketa/Walletly wallet); audio summary of NP recommendations also stored in each patient’s portal</p>
  </div>

  <div class="brand-name">Lumora Wellness</div>
  <div class="footer-copyright">©2015 Lumora Wellness • All Rights Reserved.</div>
  <div class="footer-url">LumoraWellness.example</div>
</div>
</body>
</html>
```